Business Cards that are elegant and wow

I want to create and print business cards that represent my brand and stand out from the rest. We want to ensure they stay in our branding and the integrity is not lost. I am happy to look at different shapes like square etc.

It will be printed on very thick cards and will be stylish .

I want to create and print business cards that represent my brand and stand out from the rest. We want to ensure they stay in ur branding and the integrity is not lost. I am happy to look at different shapes like square etc.

Target Market(s)

real estate professionals

Industry/Entity Type

Real Estate

Contact Information for Business Card

Maren Holt
hello@brightfernrealty.com.au
brightfernrealty.com.au
0487 316 252 (SMS)

Colors

Designer to choose colors to be used in the design.

Requirements
Must have
• My logo
• email
• website
• Name
Nice to have
• I like the idea of printing with foil or spot gloss. You want it to stand out in a sea.
Should not have
• I would like you to stay in my colour themes. Don't change the colour of my logo

```html
<!DOCTYPE html>
<html lang="en">
<head>
<meta charset="UTF-8">
<title>Bright Fern Realty – Square Business Cards</title>
<link href="https://fonts.googleapis.com/css2?family=Heebo:wght@300;400;500&display=swap" rel="stylesheet">
<style>
  :root {
    --backdrop: #e6e8eb;
    --card-black: #1a1b1d;
    --brand-blue: #29a8e0;
    --ring-blue-light: #6ab8e8;
    --ring-blue-deep: #1e86c0;
    --grad-pink: #a24a70;
    --grad-blue: #6a9fd0;
    --grad-dark: #2c2f38;
    --grad-plum: #5a4a60;
  }
  * { box-sizing: border-box; margin: 0; padding: 0; }
  html, body {
    width: 1200px;
    height: 1200px;
    overflow: hidden;
    background: var(--backdrop);
    font-family: "Heebo", "Helvetica Neue", Arial, sans-serif;
  }
  .canvas {
    position: relative;
    width: 1200px;
    height: 1200px;
  }
  .card {
    position: absolute;
    width: 560px;
    height: 560px;
    box-shadow: 0 10px 24px rgba(0, 0, 0, 0.28);
  }

  /* Front of card */
  .card--front {
    left: 60px;
    top: 60px;
    background:
      linear-gradient(to bottom, rgba(44, 47, 56, 0) 0%, rgba(44, 47, 56, 0.55) 55%, var(--grad-dark) 100%),
      linear-gradient(100deg, var(--grad-pink) 0%, #86708f 45%, var(--grad-blue) 100%);
  }
  .card--front::after {
    content: "";
    position: absolute;
    inset: 0;
    background: linear-gradient(200deg, rgba(0,0,0,0) 40%, rgba(90, 74, 96, 0.55) 100%);
    pointer-events: none;
  }
  .seal {
    position: absolute;
    left: 100px;
    top: 100px;
    width: 370px;
    height: 370px;
    border-radius: 50%;
    background: var(--card-black);
    border: 4px solid var(--ring-blue-deep);
    box-shadow: 0 0 0 1px var(--ring-blue-light) inset;
    display: flex;
    align-items: center;
    justify-content: center;
    z-index: 1;
  }

  /* Wordmark */
  .wordmark {
    display: flex;
    align-items: center;
    gap: 10px;
    color: var(--brand-blue);
    font-weight: 500;
    white-space: nowrap;
  }
  .wordmark__dot {
    border: 3px solid var(--brand-blue);
    border-radius: 50%;
    flex: none;
  }
  .wordmark__name {
    letter-spacing: 0.02em;
    text-transform: uppercase;
  }
  .seal .wordmark { font-size: 27px; }
  .seal .wordmark__dot { width: 52px; height: 52px; }

  /* Back of card */
  .card--back {
    left: 580px;
    top: 560px;
    background: var(--card-black);
    color: var(--brand-blue);
  }
  .card--back .wordmark {
    position: absolute;
    top: 100px;
    right: 50px;
    font-size: 23px;
  }
  .card--back .wordmark__dot { width: 44px; height: 44px; }
  .contact {
    position: absolute;
    right: 60px;
    top: 300px;
    text-align: right;
  }
  .contact__name {
    font-size: 40px;
    font-weight: 500;
    line-height: 1;
    margin-bottom: 20px;
  }
  .contact__line {
    font-size: 21px;
    font-weight: 300;
    line-height: 1;
    margin-bottom: 26px;
  }
</style>
</head>
<body>
  <main class="canvas">
    <section class="card card--front" aria-label="Card front">
      <div class="seal">
        <div class="wordmark">
          <span class="wordmark__dot"></span>
          <span class="wordmark__name">Bright Fern Realty</span>
        </div>
      </div>
    </section>

    <section class="card card--back" aria-label="Card back">
      <div class="wordmark">
        <span class="wordmark__dot"></span>
        <span class="wordmark__name">Bright Fern Realty</span>
      </div>
      <div class="contact">
        <p class="contact__name">Maren Holt</p>
        <p class="contact__line">hello@brightfernrealty.com.au</p>
        <p class="contact__line">brightfernrealty.com.au</p>
        <p class="contact__line">0487 316 252 (SMS)</p>
      </div>
    </section>
  </main>
</body>
</html>
```